Business Card Design

i am looking a business card for a car rental company long with Taxi service also a logo.

what is the latest with my project

Industry/Entity Type

Business

Contact Information for Business Card

name of the Company is Kestrel Bay Motor Leasing and Taxi Services
Address: Low Marsh Village, St. Aldric's Parish Antigua
Tele# 555-0142/5550187-555-0163
Email: lorimbeck@quillmarsh.test

Font styles to use
Script

```html
<!DOCTYPE html>
<html lang="en">
<head>
<meta charset="utf-8">
<title>Kestrel Bay Motor Leasing and Taxi Services – Business Card</title>
<link rel="stylesheet" href="https://fonts.googleapis.com/css2?family=Lato:wght@300;400&display=swap">
<style>
  :root {
    --page-bg: #f4f4f4;
    --card-bg: #231f20;
    --divider: #4a4647;
    --brand: #ffffff;
    --tagline: #8f8c8d;
    --contact: #e6e6e6;
    --emblem-light: #4b4748;
    --emblem-dark: #2c2829;
  }
  html, body {
    margin: 0;
    width: 1200px;
    height: 960px;
    overflow: hidden;
    background: var(--page-bg);
  }
  .canvas {
    width: 1200px;
    height: 960px;
    display: flex;
    align-items: center;
    justify-content: center;
  }
  .business-card {
    position: relative;
    width: 980px;
    height: 560px;
    background: var(--card-bg);
    box-shadow: 0 18px 40px rgba(0, 0, 0, 0.18);
    font-family: "Lato", Arial, sans-serif;
  }
  .card-divider {
    position: absolute;
    left: 50%;
    top: 0;
    width: 2px;
    height: 100%;
    background: var(--divider);
  }
  .brand-name {
    position: absolute;
    left: 60px;
    top: 170px;
    margin: 0;
    font-weight: 400;
    font-size: 58px;
    line-height: 1;
    color: var(--brand);
  }
  .vehicle-emblem {
    position: absolute;
    left: 40px;
    top: 270px;
    width: 300px;
    height: 160px;
    border-radius: 60px 90px 20px 20px;
    background: linear-gradient(180deg, var(--emblem-light), var(--emblem-dark));
    opacity: 0.7;
  }
  .tagline {
    position: absolute;
    left: 55%;
    top: 110px;
    margin: 0;
    font-weight: 400;
    font-size: 24px;
    color: var(--tagline);
  }
  .contact-details {
    position: absolute;
    left: 55%;
    top: 215px;
    margin: 0;
    font-style: normal;
    font-weight: 400;
    font-size: 18px;
    line-height: 1.6;
    color: var(--contact);
  }
</style>
</head>
<body>
  <main class="canvas">
    <section class="business-card" aria-label="Business card front">
      <h1 class="brand-name">Kestrel Bay</h1>
      <div class="vehicle-emblem" role="img" aria-label="Outline drawing of a sports car, part of the company emblem"></div>
      <div class="card-divider"></div>
      <p class="tagline">Motor Leasing &amp; Taxi Services</p>
      <address class="contact-details">
        Low Marsh Village, St. Aldric's Parish Antigua<br>
        Tele: 555-0142 / 5550187 / 555-0163<br>
        Email: lorimbeck@quillmarsh.test
      </address>
    </section>
  </main>
</body>
</html>
```